Business card for Chiropractic clinics needs reworked / redesigned

The business card in attachment was designed 10 years ago. It is in need of an update.
We have 2 clinics:
HALSPUNT VORDA & HALSPUNT MIRBE
Only one address needs to be on the card for doctors that only work in one clinic and two addresses need to be on the card for the doctors that work in both clinics.

Target Market(s)

patients/referrers

Industry/Entity Type

Medical

Contact Information for Business Card

Logo (in full or zoomed-in)
Clinic Name
Doctor name and title
clinic address, website, tel, email

Font styles to use
Sans Serif

Colors

Designer to choose colors to be used in the design.

Requirements
Must have
• Good contrast/readability
• We like modern minimalistic designs
• The Bcard needs to project our very high standard of proficiency/professionalism
Should not have
• Not curly
• Not to much colours

```html
<!DOCTYPE html>
<html lang="en">
<head>
<meta charset="utf-8">
<title>Halspunt business card</title>
<link href="https://fonts.googleapis.com/css2?family=Lato:wght@300;400;700&display=swap" rel="stylesheet">
<style>
  :root {
    --backdrop: #e6e8e7;
    --clinic-green: #1f3d38;
    --card-white: #ffffff;
    --logo-grey: #9a9a9a;
    --ink: #2b2b2b;
    --on-green: #ffffff;
  }
  html, body {
    margin: 0;
    padding: 0;
    width: 1200px;
    height: 900px;
    overflow: hidden;
    background: var(--backdrop);
    font-family: "Lato", Arial, sans-serif;
  }
  .canvas {
    position: relative;
    width: 1200px;
    height: 900px;
  }
  .card {
    position: absolute;
    width: 620px;
    height: 354px;
    box-sizing: border-box;
    box-shadow: 0 10px 28px rgba(0,0,0,0.18);
  }
  /* front */
  .card-front {
    left: 110px;
    top: 60px;
    background: var(--clinic-green);
    color: var(--on-green);
  }
  .front-brand {
    position: absolute;
    right: 60px;
    top: 92px;
    text-align: center;
  }
  .front-name {
    font-weight: 300;
    font-size: 52px;
    letter-spacing: 1px;
    line-height: 1;
  }
  .front-locations {
    font-weight: 300;
    font-size: 28px;
    letter-spacing: 1px;
    margin-top: 8px;
  }
  .front-web {
    font-size: 14px;
    letter-spacing: 1px;
    margin-top: 40px;
  }
  /* back */
  .card-back {
    left: 470px;
    top: 476px;
    background: var(--card-white);
    border-bottom: 10px solid var(--clinic-green);
    color: var(--ink);
  }
  .back-brand {
    position: absolute;
    left: 44px;
    top: 68px;
    font-weight: 300;
    font-size: 50px;
    letter-spacing: 1px;
    color: var(--logo-grey);
    line-height: 1;
  }
  .doctor {
    position: absolute;
    left: 44px;
    bottom: 42px;
  }
  .doctor-name {
    font-weight: 700;
    font-size: 24px;
    color: var(--clinic-green);
  }
  .doctor-title {
    font-size: 15px;
    margin-top: 4px;
  }
  .contact {
    position: absolute;
    left: 370px;
    top: 84px;
    font-size: 14px;
    line-height: 1.3;
  }
  .clinic-address {
    margin-bottom: 8px;
  }
  .contact-line {
    display: flex;
    align-items: center;
    gap: 10px;
    margin-top: 3px;
  }
  .contact-line svg {
    width: 12px;
    height: 12px;
    flex: none;
    fill: var(--clinic-green);
  }
</style>
</head>
<body>
<div class="canvas">

  <section class="card card-front">
    <div class="front-brand">
      <div class="front-name">HALSPUNT</div>
      <div class="front-locations">VORDA - MIRBE</div>
      <div class="front-web">www.halspuntvorda.be</div>
    </div>
  </section>

  <section class="card card-back">
    <div class="back-brand">HALSPUNT</div>

    <div class="contact">
      <div class="clinic-address">Halspunt Mirbe<br>Lindenlaan 41, 8000 Mirbe</div>
      <div class="clinic-address">Halspunt Vorda<br>Kouterweg 118, 9000 Vorda</div>
      <div class="contact-line">
        <svg viewBox="0 0 24 24" aria-hidden="true"><path d="M6.6 10.8a15.1 15.1 0 0 0 6.6 6.6l2.2-2.2a1 1 0 0 1 1-.25 11.4 11.4 0 0 0 3.6.57 1 1 0 0 1 1 1V20a1 1 0 0 1-1 1A17 17 0 0 1 3 4a1 1 0 0 1 1-1h3.5a1 1 0 0 1 1 1c0 1.25.2 2.45.57 3.57a1 1 0 0 1-.25 1z"/></svg>
        <span>+32 (0)9 480 13 52</span>
      </div>
      <div class="contact-line">
        <svg viewBox="0 0 24 24" aria-hidden="true"><path d="M2 5h20v14H2z M2 5l10 8 10-8" fill="none" stroke="#1f3d38" stroke-width="2.4"/></svg>
        <span>info@halspuntvorda.be</span>
      </div>
      <div class="contact-line">
        <svg viewBox="0 0 24 24" aria-hidden="true"><circle cx="12" cy="12" r="10" fill="none" stroke="#1f3d38" stroke-width="2.4"/><path d="M2 12h20M12 2c3 3 3 17 0 20M12 2c-3 3-3 17 0 20" fill="none" stroke="#1f3d38" stroke-width="2"/></svg>
        <span>www.halspuntvorda.be</span>
      </div>
    </div>

    <div class="doctor">
      <div class="doctor-name">Elias Vanderhaegen D.C.</div>
      <div class="doctor-title">Chiropractor</div>
    </div>
  </section>

</div>
</body>
</html>
```